Mobile Repair Service on location needs a Web Design

We are starting a new mobile device repair service called Gadget Haven and our website needs a design!

Hello Designers!
First, we'd like to make clear this is more than a simple web design contest, we want the designers to create an idea. We want someone who can create the whole theme of the service's we provide. We want someone that can help design our visual branding, help us communicate a sentiment. And we are willing to pay for that.

Who are we?
Our company is based in Rotterdam, the Netherlands. We provide different services for all kinds of electronic devices. The kind of services we provide are, among other things, installations of hardware and software and the repair of broken or malfunctioning devices.
We are starting a new service that offers mobile device repairs on location, be it at the home of our customers, their office, or any other place. Just give us the address and we will come to you for the repair job. This is also our main USP. We have multiple skilled engineers who drive trough the country on a daily basis and can be on location within a working day. Repair is done immediately onsite while the customer waits. At this stage we will start with the smartphone product-group within the mobile devices. In a second phase we might also add tablets.
People don't want to be without their phone for weeks because of some parts that needed to be ordered by a repair center they had to sent their phone to. We offer a fully functional mobile repair center in the form of specially customized vans. These vans have all the tools and utilities needed by our engineers to safely repair your mobile device. Your phone is being repaired directly in front of you, the next business-day, on a location you desire.

For this new service we are creating a website called Gadget Haven. The website needs a story and matching design and this is where you come in. We are not looking for a simple template design we can get from any place. We need a story. We want you to create an idea, build a unique theme or vision that helps sell the product/service. This goes beyond the design of the website. We need the whole package, the design you are creating needs to have returning elements like icons, color use, images, maybe even characters etc. You name it! There needs to be a common thread in the design so we can reuse elements in, for example, the email templates, the work order or receipt we give to our customers (we may contact the winner of the contest to design these for us as well!).

The name 'Gadget Haven' is chosen. Haven (short for rehabilitate) has a bold and playful tone to it and the design needs to reflect the name. So we're looking for a somewhat playful and cheeky design. Definitely not too serious and definitely modern. We already got a logo that we love and that fit's this description (see attached design documents for the logo). It's bold, powerful and fun. Our web design needs to reflect this as well and has to fit in with our logo.
We would really like it if the design somehow incorporates elements that highlight our unique selling points (repairs on location, we come to you etc.). We would really like some form of story telling in the design. Think clumsy people breaking their phones. Teenagers in tears because they have no access to their friends. People nowadays have the need to always be 'connected'. What happens when your phone is broken or malfunctioning? We're handling tech, we are nerds and a little bit weird, but we're professionals and here to help you with your problem. The sentiment Wire Troop tries to communicate is something we really like. We're looking for fresh idea's, anything goes!

In an overview all Unique Selling Points of the Gadget haven service:
- Professional service on location. Don’t ship to us we will come to you!
- Clear pricing upfront. No hidden cost.
- Next business-day repair.
- Backed by a professional call center open 12 hours a day and open on a Saturday as well
- Backed by a professional repair center with more then 12 years of experience
- Repair is done by certified engineers
- 1 year warranty on the repair

The process:
The main function of our website will be for customers to make a repair request. A customer will visit our website and can make a repair request immediately by going through a 'request-order-flow'. In this flow he or she will need to fill in some forms and can select wich type/model/brand of mobile device he or she has and what parts need to be repaired. After a request is placed we will call the customer back (within an hour) for a short intake and to set a date/time and location. Our engineer will meet the customer at the specified location and will repair the device onsite in one of our mobile repair centers, which is a specialized van equipped with all the tools needed for device restorations.
So in short the steps are:
- Choose your device and repair job
- Place the order
- Get a callback within the hour
- Set date and location
- We will come to you.

Website functionality:
Our website is our main form of communication. So the sentiment we want to communicate needs be reflected in the design. We need a main/front page designed (preferably a long scrolling page design) containing:
1. Customers will be able to request a repair job directly on our website. So there will need to be a prominent button/link at the top of our main page that will bring the customer to this 'request-order-flow'. This is the main flow which needs to be full focus on the front page. All other items are secondary.
2. The general information of who we are and what we do, and why the customer should choose us. Preferably in short bullet-point type keywords/sentences with icons or other visual cues. See our unique selling points to get an idea of the information that will be displayed here.
3. There needs to be a section that will explain the process (see above) of a repair request step-by- step, again in brief short key sentences and with (custom) icons.
4. There needs to be a section that explains to the customer he/she can always contact us if they are not sure what the problem is with their device, and for this reason are not sure what repair request they should order.
5. We want to implement some functionality that display customer ratings or customer reviews. So there needs to be room for some kind of widget of plugin we're going to implement which shows these reviews.
6. A 'For business section' where we will explain all the options we provide for corporate clients.
7. Social media links.
8. There needs to be a menu with buttons that leads to the all sections described in the previous points.

For now, we need a design for our front page. In the second phase, when we have picked our winner, we may ask the winner to design the page(s) for our request workflow as well.

EDIT:
Finally, we have a very specific order in mind for the different segments of our website. We would like you to add some more segments that were not in our original brief as well:

1. Top header with order/request button. (should instantly make clear our main USP, we do repairs on location)
2. Our process
3. Our unique selling points / why choose us
4. The kind of repairs we do (broken screens, broken batteries, water damage, broken camera's, no sound etc.)
5. A 'meet our team' section, where we introduce some of our engineers
6. A 'contact us for any questions' section/
7. Testimonials/user reviews
8. A section where we show key performance indicators
9. 'For businesses' sections
10.'Subscribe for newsletter' field
11. Social media buttons

Industry/Entity Type

It Service

Number of Pages Required

1 page

Font styles to use
Sans Serif

Requirements
Must have
• a main/front page, design only
• custom icons/images for banners, adverts online and in print (high res)
Nice to have
• Storytelling in our design.
• Design that fits with our brand new logo.
• Elements like icons to have a flat design.
• Keep in mind that the website will need to be responsive when designing! (Ideally provide an example of the mobile design as well)
• Create a fun and trustworthy feeling.

```html
<!DOCTYPE html>
<html lang="en">
<head>
<meta charset="UTF-8">
<title>Gadget Haven – We will come to you</title>
<link href="https://fonts.googleapis.com/css2?family=Ubuntu:wght@300;400;500;700&display=swap" rel="stylesheet">
<style>
  :root {
    --green: #16b84e;
    --green-dark: #0f9a3f;
    --ink: #222222;
    --ink-soft: #3a3a3a;
    --white: #ffffff;
    --mist: #f7f7fc;
    --hero-dark: #2b2930;
    --hero-mid: #4a4650;
    --orange: #e8572a;
  }
  * { margin: 0; padding: 0; box-sizing: border-box; }
  html, body { width: 800px; height: 1200px; overflow: hidden; background: var(--white); }
  body { font-family: "Ubuntu", sans-serif; color: var(--ink); position: relative; }

  .brand { position: absolute; left: 14px; top: 40px; display: flex; align-items: center; gap: 10px; }
  .brand-mark { width: 26px; height: 26px; background: var(--orange); border-radius: 50%; }
  .brand-name { font-weight: 700; font-size: 27px; line-height: 1; color: var(--ink-soft); letter-spacing: 0.5px; }
  .brand-tagline { position: absolute; left: 50px; top: 76px; font-size: 10px; font-weight: 500; color: #2a3f8f; }

  .call-top { position: absolute; left: 277px; top: 14px; display: flex; align-items: center; gap: 10px; }
  .call-top svg { width: 40px; height: 40px; }
  .call-top .label { font-weight: 500; font-size: 40px; color: var(--ink-soft); letter-spacing: 0.5px; }
  .call-top .number { font-weight: 300; font-size: 38px; color: var(--green); margin-left: 24px; }

  .main-nav { position: absolute; top: 64px; left: 267px; width: 520px; display: flex; justify-content: space-between; }
  .main-nav a { font-weight: 500; font-size: 26px; color: var(--green); text-decoration: none; display: flex; align-items: center; gap: 4px; }
  .main-nav a::after { content: ""; border: 5px solid transparent; margin-top: 6px; }
  .main-nav a.is-link::after { border-left: 7px solid var(--ink); border-right: 0; }
  .main-nav a.has-menu::after { border-top: 7px solid var(--ink); border-bottom: 0; margin-top: 10px; }

  .hero { position: absolute; left: 13px; top: 106px; width: 773px; height: 422px; overflow: hidden; }
  .hero-photo { position: absolute; inset: 0; background: linear-gradient(160deg, var(--hero-mid) 0%, var(--hero-dark) 55%, #3c3a40 100%); }
  .hero-title { position: absolute; top: 52px; left: 0; right: 0; text-align: center; color: var(--white); font-weight: 700; font-size: 28px; margin-left: 160px; margin-right: 100px; }
  .hero-sub { position: absolute; top: 88px; left: 0; right: 0; text-align: center; color: var(--white); font-weight: 500; font-size: 18px; margin-left: 160px; margin-right: 100px; }

  .request-form { position: absolute; left: 12px; top: 121px; width: 225px; height: 293px; background: var(--green); }
  .request-form h2 { position: absolute; left: 8px; top: 18px; color: var(--white); font-weight: 500; font-size: 22px; white-space: nowrap; }
  .field { position: absolute; width: 92px; height: 47px; background: var(--white); font-size: 8px; color: var(--ink); padding: 18px 10px 0; }
  .send-btn { position: absolute; left: 17px; top: 232px; width: 190px; height: 43px; background: #000; color: var(--white); font-weight: 500; font-size: 18px; display: flex; align-items: center; justify-content: center; }

  .why { position: absolute; left: 13px; top: 528px; width: 773px; height: 260px; background: var(--mist); }
  .why h2 { position: absolute; left: 15px; top: 12px; font-weight: 500; font-size: 40px; color: var(--green); }
  .why ul { position: absolute; left: 12px; top: 68px; list-style: none; }
  .why li { font-size: 17.5px; line-height: 22px; color: var(--ink); padding-left: 12px; position: relative; }
  .why li::before { content: ""; position: absolute; left: 0; top: 8px; width: 7px; height: 8px; border-radius: 50%; background: var(--green); }

  .service h2 { position: absolute; left: 29px; top: 835px; font-weight: 700; font-size: 42px; color: var(--ink); white-space: nowrap; }
  .service h2 span { color: var(--green); margin-left: 8px; }
  .service p { position: absolute; left: 38px; top: 912px; font-weight: 500; font-size: 25px; line-height: 33px; color: var(--ink); }

  .call-band { position: absolute; left: 13px; top: 1088px; width: 773px; height: 92px; background: var(--green); color: var(--white); font-weight: 500; font-size: 42px; display: flex; align-items: center; justify-content: center; letter-spacing: 0.5px; }
</style>
</head>
<body>
  <header>
    <div class="brand">
      <span class="brand-mark"></span>
      <span class="brand-name">GADGET HAVEN</span>
    </div>
    <div class="brand-tagline">We will come to you!</div>

    <div class="call-top">
      <svg viewBox="0 0 40 40" aria-hidden="true">
        <circle cx="20" cy="20" r="16" fill="none" stroke="#16b84e" stroke-width="3"/>
        <path d="M15 12c-2 1-3 3-2 6 1 4 4 8 8 10 3 1 5 0 6-2l-3-3-2 1c-2-1-4-3-5-5l1-2z" fill="#16b84e"/>
      </svg>
      <span class="label">CALL US</span>
      <span class="number">(010) 555-0142</span>
    </div>

    <nav class="main-nav">
      <a class="is-link">Home</a>
      <a class="has-menu">Custom</a>
      <a class="has-menu">Service Centre</a>
    </nav>
  </header>

  <section class="hero">
    <div class="hero-photo" role="img" aria-label="Technician's hands repairing opened smartphones with a multimeter on a workbench"></div>
    <h1 class="hero-title">PHONE PROBLEMS?</h1>
    <p class="hero-sub">We will come to you</p>

    <form class="request-form">
      <h2>Request-order-flow</h2>
      <div class="field" style="left:17px;top:61px">First Name</div>
      <div class="field" style="left:115px;top:61px">Last Name</div>
      <div class="field" style="left:17px;top:119px">E-mail</div>
      <div class="field" style="left:115px;top:119px">Phone</div>
      <div class="field" style="left:17px;top:175px">Problems</div>
      <div class="field" style="left:115px;top:175px">Service Centre</div>
      <div class="send-btn">Send a message</div>
    </form>
  </section>

  <section class="why">
    <h2>Why Choose Us?</h2>
    <ul>
      <li>Professional service on location. Don’t ship to us we will come to you!</li>
      <li>Clear pricing upfront. No hidden cost.</li>
      <li>Next business-day repair.</li>
      <li>Backed by a professional call center open 12 hours a day and open on a Saturday as well.</li>
      <li>Backed by a professional repair center with more then 12 years of experience.</li>
      <li>Repair is done by certified engineers.</li>
      <li>1 year warranty on the repair.</li>
    </ul>
  </section>

  <section class="service">
    <h2>OUR SERVICE<span>IS BEST</span></h2>
    <p>We shall provide a care for every budget.<br>
       One stop solution for all makes and models.<br>
       Free estimates with friendly service.</p>
  </section>

  <div class="call-band">CALL US (010) 555-0142</div>
</body>
</html>
```